Qualifying Builders Questionnaire

We need a questionnaire designed to send out to potential clients with qualifying questions

Industry/Entity Type

Building

Colors

Designer to choose colors to be used in the design.

```html
<!DOCTYPE html>
<html lang="en">
<head>
<meta charset="utf-8">
<title>Qualifying Builders Questionnaire</title>
<link rel="stylesheet" href="https://fonts.googleapis.com/css2?family=Roboto:wght@400;500&display=swap">
<style>
  :root {
    --page-bg: #f3f0f0;
    --column-bg: #ffffff;
    --panel-bg: #f8f8f8;
    --panel-border: #e7e5e5;
    --question-ink: #333333;
    --option-ink: #6b6b6b;
    --box-border: #c4c4c4;
    --box-fill: #ffffff;
    --note-red: #e2262b;
  }
  html, body {
    margin: 0;
    padding: 0;
    width: 1200px;
    height: 773px;
    overflow: hidden;
    background: var(--page-bg);
    font-family: "Roboto", Arial, sans-serif;
  }
  .canvas {
    position: relative;
    width: 1200px;
    height: 773px;
    overflow: hidden;
  }
  .column {
    position: absolute;
    left: 71px;
    width: 1058px;
    top: 0;
    bottom: 0;
    background: var(--column-bg);
  }
  .form-panel {
    position: absolute;
    left: 106px;
    width: 988px;
    top: -2px;
    bottom: -2px;
    background: var(--panel-bg);
    border-left: 1px solid var(--panel-border);
    border-right: 1px solid var(--panel-border);
  }
  .question {
    position: absolute;
    left: 138px;
    margin: 0;
    font-size: 24px;
    font-weight: 500;
    color: var(--question-ink);
    line-height: 1;
    transform: translateY(-50%);
    white-space: nowrap;
  }
  .option {
    position: absolute;
    display: flex;
    align-items: center;
    transform: translateY(-50%);
    font-size: 22px;
    color: var(--option-ink);
    white-space: nowrap;
  }
  .checkbox {
    width: 33px;
    height: 33px;
    box-sizing: border-box;
    border: 1.5px solid var(--box-border);
    background: var(--box-fill);
    margin-right: 20px;
    flex: none;
  }
  .follow-up-note {
    position: absolute;
    left: 136px;
    top: 717px;
    transform: translateY(-50%);
    margin: 0;
    font-size: 21px;
    color: var(--note-red);
    text-decoration: underline;
    text-underline-offset: 3px;
    white-space: nowrap;
  }
</style>
</head>
<body>
<main class="canvas">
  <div class="column"></div>
  <section class="form-panel"></section>

  <h2 class="question" style="top:65px">What does you enquiry relate to? *</h2>
  <label class="option" style="left:134px; top:139px"><span class="checkbox"></span>House design, build &amp; certification</label>
  <label class="option" style="left:134px; top:218px"><span class="checkbox"></span>Renovation</label>
  <label class="option" style="left:134px; top:298px"><span class="checkbox"></span>Extension</label>
  <label class="option" style="left:134px; top:376px"><span class="checkbox"></span>Elmwood Home design &amp; build</label>
  <label class="option" style="left:134px; top:455px"><span class="checkbox"></span>Other...</label>

  <h2 class="question" style="top:551px">Have you obtained any plans or documentation for your project? *</h2>
  <label class="option" style="left:134px; top:627px"><span class="checkbox"></span>Yes</label>
  <label class="option" style="left:275px; top:627px"><span class="checkbox"></span>No</label>

  <p class="follow-up-note">If yes, please select from the following list to indicate what you have</p>
</main>
</body>
</html>
```